AMAZING WEBSITE DESIGN NEEDED FOR MAID / CLEANING SERVICE

NOTE: This is Website Design Only - No coding required

Please submit your designs ASAP as we want to pick a winner and get started!

Hey,

We are looking for a new amazing website design for a maid or cleaning service.

They have a horrible website that we want turned into a masterpiece.

As you will see on their current site:

http://tidyhavenco.examplehost.net/

They have a lot of stuff, very disorganized, and need help.

Here is what we need:

Colors: Same as current site, Orange, Gray, Black

Menu: Horizontal with same Menu items

Need a spot for a video on the homepage

Want content to be structured in a great format that is easy to read.

Want to highlight commercial and residential on the website homepage.

Also want a spot for customer testimonials

We want the site clean, professional, fresh and modern.

Please help by matching the logo design.

I look forward to your designs!
Updates

Hi All! Really appreciate your efforts and designs. I will be meeting with our client on Monday and will then be able to provide feedback after our meeting. If you have other ideas, please submit them. The more I can show him the better! Thanks!

Target Market(s)

The target market is residential home owners as well as commercial businesses who need cleaning on a regular basis.

This company cleans homes and offices for individuals.

Industry/Entity Type

Residential

Font styles to use
Sans Serif

Requirements
Must have
• Must match logo colors
Must have spot for video
Must have a clean look
Must have a bold look
Nice to have
• Highly visual
Should not have
• clutter
messy design
hard to read

```html
<!DOCTYPE html>
<html lang="en">
<head>
<meta charset="utf-8">
<title>Tidy Haven — Quality Commercial &amp; Residential Cleaning</title>
<link rel="stylesheet" href="https://fonts.googleapis.com/css2?family=Arimo:ital,wght@0,400;0,700;1,400;1,700&display=swap">
<style>
:root{
  --orange:#ff7f00;
  --orange-light:#ffa31a;
  --orange-dark:#f06c00;
  --gray-dark:#5f5f5f;
  --gray-mid:#6b6b6b;
  --gray-bar:#707070;
  --gray-line:#d9d9d9;
  --gray-soft:#f4f2f2;
  --gray-bg:#f2f2f2;
  --text:#555;
  --white:#fff;
}
*{box-sizing:border-box;margin:0;padding:0}
html,body{width:1200px;height:2410px;overflow:hidden}
body{font-family:"Arimo",Arial,sans-serif;color:var(--text);background:var(--gray-bg);position:relative}
.backdrop{position:absolute;left:0;top:0;width:1200px;height:2410px}
.page{position:absolute;left:86px;top:34px;width:1020px;height:2342px;background:var(--white);box-shadow:0 0 8px rgba(0,0,0,.25)}
.abs{position:absolute}

/* top bar */
.topbar{left:0;top:0;width:1020px;height:40px;background:linear-gradient(#7a7a7a,#5c5c5c);border-bottom:3px solid var(--orange);color:var(--white);font-size:12px;text-align:right;padding:13px 28px 0 0}

/* header */
.brand{left:45px;top:58px}
.brand-row{display:flex;align-items:center;gap:10px}
.brand-mark{width:26px;height:26px;background:var(--orange)}
.brand-name{font-size:32px;font-weight:700;color:var(--orange);letter-spacing:-.5px}
.brand-tag{font-size:11px;font-style:italic;font-weight:700;color:var(--orange);margin-top:6px;margin-left:36px}
.socials{display:flex;gap:8px}
.social{width:26px;height:26px;border-radius:50%;background:var(--orange)}
.header-social{left:839px;top:98px}
.call{right:47px;top:136px;font-size:13px;color:#333;font-weight:700}
.call span{font-size:21px;color:var(--orange);font-weight:400;margin-left:8px}

/* nav */
.nav{left:45px;top:172px;width:928px;height:49px;display:flex;background:linear-gradient(#7e7e7e,#5d5d5d);border-radius:3px;overflow:hidden}
.nav a{display:flex;align-items:center;justify-content:center;color:var(--white);font-size:14px;text-decoration:none;border-right:1px solid #8a8a8a}
.nav a:last-child{border-right:none}
.nav .active{background:linear-gradient(var(--orange-light),var(--orange))}

/* hero */
.hero{left:45px;top:236px;width:928px;height:363px;overflow:hidden}
.hero-photo{position:absolute;inset:0;background:linear-gradient(120deg,#e9e1d2 0%,#c9b89c 30%,#2f4f8c 50%,#26407a 62%,#d8c6a8 85%)}
.hero-panel{position:absolute;right:0;top:0;width:300px;height:363px}
.hero-copy{position:absolute;right:22px;top:50px;width:240px;color:var(--white)}
.hero-copy h1{font-weight:400;font-size:25px;line-height:33px}
.hero-copy p{font-size:12px;line-height:20px;margin-top:8px}
.hero-copy .more{font-style:italic;font-weight:700;font-size:12px;margin-top:6px}
.dots{display:flex;gap:4px;margin-top:18px}
.dots i{width:14px;height:14px;border-radius:50%;background:var(--white)}

.section-title{font-size:20px;color:var(--orange);font-weight:400}

/* video */
.video{left:45px;top:680px;width:612px;height:302px;border-radius:4px;overflow:hidden;background:linear-gradient(160deg,#d9dcb2 0%,#c6c79d 35%,#a39c88 60%,#8b8478 100%)}
.video-actions{position:absolute;right:10px;top:12px;display:flex;flex-direction:column;gap:4px}
.video-actions span{width:38px;height:30px;background:#3a3a3a;border-radius:3px;color:var(--white);font-size:7px;font-weight:700;text-align:center;padding-top:18px}
.video-bar{position:absolute;left:14px;right:14px;bottom:10px;height:34px;background:rgba(40,40,40,.85);border-radius:4px}
.play{position:absolute;left:0;top:0;width:60px;height:34px;background:#2a2a2a;border-radius:4px}
.track{position:absolute;left:78px;top:14px;width:392px;height:6px;background:#999;border-radius:3px}
.track b{display:block;width:140px;height:6px;background:#ddd;border-radius:3px}
.time{position:absolute;left:210px;top:-16px;background:#222;color:#fff;font-size:9px;padding:2px 4px;border-radius:2px}
.hd{position:absolute;right:26px;top:11px;font-size:10px;font-style:italic;font-weight:700;color:var(--orange)}
.video-caption{left:45px;top:992px;width:612px;height:54px;background:linear-gradient(#f1f1f1,#fff);font-size:13.5px;line-height:21px;padding:4px 4px;color:#555}

/* offer form */
.offer{left:680px;top:680px;width:293px;height:346px;background:#f4f4f4;border:1px solid #e6e6e6}
.offer h2{height:42px;background:linear-gradient(var(--orange-light),var(--orange));color:var(--white);font-size:18px;font-weight:700;text-align:center;padding-top:11px}
.offer h2 em{font-style:italic}
.field{margin:18px 25px 0;height:34px;border:1px solid #ccc;background:var(--white);font-size:11px;color:#aaa;padding:10px 12px}
.field.focus{border:2px solid #9ab8d8}
.field + .field{margin-top:16px}
.field sup{color:var(--orange)}
.optin{display:flex;gap:8px;margin:22px 25px 0;font-size:11px;line-height:16px;color:#888}
.optin i{flex:none;width:11px;height:11px;border:1px solid #999;background:#ddd;margin-top:3px}
.optin b{color:#666}
.send{margin:12px 25px 0;height:40px;background:linear-gradient(var(--orange-light),var(--orange));color:var(--white);font-weight:700;font-size:15px;text-align:center;padding-top:12px;letter-spacing:1px}

/* services */
.service{top:1163px;width:258px}
.service-photo{height:117px;border:1px solid #ddd}
.service h3{font-size:19px;font-weight:400;color:var(--orange);margin-top:19px}
.service p{font-size:13.5px;line-height:21px;color:#555;margin-top:4px;height:96px}
.btn{display:block;width:150px;height:38px;background:linear-gradient(var(--orange-light),var(--orange));color:var(--white);font-size:14px;text-align:center;padding-top:11px;border-radius:2px}
.divider{top:1190px;width:1px;height:290px;background:linear-gradient(transparent,#e3e3e3,transparent)}

/* about */
.about{left:45px;top:1567px;width:566px}
.about p{font-size:13.5px;line-height:25px;color:#555;margin-top:8px}
.about p:first-of-type{margin-top:12px}
.why{left:653px;top:1550px;width:320px;height:358px;background:var(--gray-soft)}
.why h2{height:44px;background:#ece9e9;text-align:center;padding-top:12px}
.why ul{list-style:none;padding:14px 20px 0 16px}
.why li{display:flex;gap:14px;margin-bottom:18px}
.why li i{flex:none;width:11px;height:11px;border-radius:50%;border:3px solid var(--orange);margin-top:4px}
.why strong{display:block;font-size:14px;color:#444;font-weight:400}
.why span{display:block;font-size:13.5px;line-height:21px;color:#555}

/* go up */
.goup{left:827px;top:1974px;width:141px;height:34px;background:linear-gradient(#7a7a7a,#5d5d5d);color:var(--white);font-size:14px;display:flex;border-radius:3px 3px 0 0;overflow:hidden}
.goup .arrow{width:44px;background:#555;display:flex;align-items:center;justify-content:center}
.goup .label{flex:1;text-align:center;padding-top:9px}

/* footer */
.footer{left:0;top:2008px;width:1020px;height:334px;background:var(--gray-mid);border-top:3px solid var(--orange);color:var(--white)}
.fcol{top:36px}
.fcol h4{font-size:14px;font-weight:400;color:var(--orange);margin-bottom:14px}
.fcol li{list-style:none;font-size:12.5px;line-height:25px}
.fbrand{right:52px;top:38px;text-align:right}
.fbrand .brand-name{font-size:26px;color:var(--white)}
.fbrand .brand-row{justify-content:flex-end}
.fbrand .brand-mark{width:22px;height:22px;background:var(--white)}
.fbrand .tag{font-size:9px;font-style:italic;font-weight:700;margin-top:4px}
.faddr{right:52px;top:118px;text-align:right;font-size:12.5px;line-height:20px;font-weight:700;font-style:normal}
.badge{left:52px;top:178px;width:86px;height:32px;background:#2b5d8c;border-radius:3px}
.fine{left:52px;top:226px;width:690px;font-size:9px;line-height:14px}
.footer-social{right:52px;top:254px}
.footer-social .social{width:24px;height:24px}
</style>
</head>
<body>

<svg class="backdrop" viewBox="0 0 1200 2410" aria-hidden="true">
  <path d="M0 200 Q40 160 86 175 L86 2300 L0 2300 Z" fill="var(--orange)"/>
  <path d="M1106 140 Q1160 138 1200 152 L1200 2300 L1106 2300 Z" fill="var(--orange)"/>
</svg>

<div class="page">
  <div class="abs topbar">Tidy Haven, 4120 Maple Ridge Avenue Suite 310,&nbsp; Springfield, Oregon, 97477</div>

  <div class="abs brand">
    <div class="brand-row"><span class="brand-mark"></span><span class="brand-name">Tidy Haven</span></div>
    <div class="brand-tag">Quality Commercial &amp; Residential Cleaning</div>
  </div>
  <div class="abs socials header-social"><i class="social"></i><i class="social"></i><i class="social"></i><i class="social"></i></div>
  <div class="abs call">Call Us: <span>(555) 014-2290</span></div>

  <nav class="abs nav">
    <a class="active" style="width:110px">Home</a>
    <a style="width:136px">Our Services</a>
    <a style="width:117px">About Us</a>
    <a style="width:128px">Testimonials</a>
    <a style="width:163px">Why Choose Us</a>
    <a style="width:141px">Special Offers</a>
    <a style="width:133px">Contact Us</a>
  </nav>

  <section class="abs hero">
    <div class="hero-photo" role="img" aria-label="Bright tidy living room with a blue sofa, patterned cushions, a lamp and a glossy wooden floor"></div>
    <svg class="hero-panel" viewBox="0 0 300 363" aria-hidden="true">
      <defs><linearGradient id="panelFill" x1="0" y1="0" x2="0" y2="1"><stop offset="0" stop-color="#ff9a10"/><stop offset="1" stop-color="#ff7a00"/></linearGradient></defs>
      <path d="M30 0 L300 0 L300 363 L30 363 Q0 180 30 0 Z" fill="url(#panelFill)"/>
    </svg>
    <div class="hero-copy">
      <h1>Wouldn't Be Nice<br>To Come Home<br>To A Perfetly<br>Clean House!</h1>
      <p>Lorem ipsum dolor sit amet, consectetur adipisicing elit, sed do eiusmod tempor incididunt ut labore et dolore</p>
      <div class="more">Learn more...</div>
      <div class="dots"><i></i><i></i><i></i><i></i></div>
    </div>
  </section>

  <h2 class="abs section-title" style="left:45px;top:646px">Video Presentation</h2>
  <div class="abs video" role="img" aria-label="Video still of a hand wiping a granite counter with a yellow cloth">
    <div class="video-actions"><span>LIKE</span><span>SHARE</span><span>EMBED</span></div>
    <div class="video-bar">
      <div class="play"><svg width="60" height="34" viewBox="0 0 60 34"><path d="M25 10 L36 17 L25 24 Z" fill="#fff"/></svg></div>
      <div class="track"><b></b><span class="time">00:34</span></div>
      <span class="hd">HD</span>
    </div>
  </div>
  <p class="abs video-caption">Lorem ipsum dolor sit amet, consectetur adipisicing elit, sed do eiusmod tempor incididunt ut unif labore et dolore magna aliqua.</p>

  <form class="abs offer">
    <h2>Sing Up For <em>Special Offers!</em></h2>
    <div class="field focus">Name <sup>*</sup></div>
    <div class="field">Email <sup>*</sup></div>
    <div class="field">Phone</div>
    <div class="optin"><i></i><span><b>Yes!</b> I want to recive, from time to time, great Special Offers from <b>Tidy Haven</b>!</span></div>
    <div class="send">SEND</div>
  </form>

  <h2 class="abs section-title" style="left:45px;top:1126px">About Our Services</h2>

  <article class="abs service" style="left:45px">
    <div class="service-photo" role="img" aria-label="Gloved hands cleaning a green surface with a spray bottle and sponge" style="background:linear-gradient(135deg,#8fc24a,#d63a2f 55%,#f1d54a)"></div>
    <h3>Eco Friendly</h3>
    <p>Tidy Haven is commited to using Eco Green chemicals to keep you and your family safe!<br>No harsh chemicals here!</p>
    <span class="btn">Read More</span>
  </article>
  <div class="abs divider" style="left:342px"></div>
  <article class="abs service" style="left:374px">
    <div class="service-photo" role="img" aria-label="Kitchen counter being cleaned beside a potted plant" style="background:linear-gradient(135deg,#d8d4cc,#9aa39a 45%,#e7c93a 75%,#c8c2b6)"></div>
    <h3>Certified</h3>
    <p>Duis aute irure dolor in reprehenderit in voluptate velit esse cillum dolore eu fugiat nulla pariatur.</p>
    <span class="btn">Read More</span>
  </article>
  <div class="abs divider" style="left:676px"></div>
  <article class="abs service" style="left:708px">
    <div class="service-photo" role="img" aria-label="Glass office tower against a blue sky" style="background:linear-gradient(135deg,#cfe4f7,#4a86c8 50%,#1d3f78)"></div>
    <h3>Other Feature</h3>
    <p>Duis aute irure dolor in reprehenderit in voluptate velit esse cillum dolore eu fugiat nulla pariatur.</p>
    <span class="btn">Read More</span>
  </article>

  <section class="abs about">
    <h2 class="section-title">About Us</h2>
    <p>Thank you for visiting us! You are one step closer to experiencing first class maid service! Our company specializes in detailed housekeeping, janitorial, and commerical cleaning services making your environment shine and sparkle like it never has before!</p>
    <p>Our maids are fully trained professionals who we recruit from high end luxury hotels we know, like the Crestmoor and Belhaven! We pride ourselves in delivering exceptional service to our valued customers by fully understanding what your expectations &amp; needs are! We will strive for perfection and we will provide an uncompromising commitment to excellence!</p>
    <p>Our "haven" promise gives us an edge over our competition by giving you access to more home and office cleaning services for absolutely no extra costs! Why pay more for less?? NEVER have any hidden charges, overages, or sneaky fees! With Tidy Haven start getting more for your dollar! Your wish is our command and that is the true "Haven" way! Call us today!</p>
  </section>

  <aside class="abs why">
    <h2 class="section-title">Why Us</h2>
    <ul>
      <li><i></i><div><strong>Lorem ipsum dolor sit amet.</strong><span>Ut enim ad minim veniam, quis nostrud exercitation ullamco laboris nisi ut aliquip ex ea commodo consequat.</span></div></li>
      <li><i></i><div><strong>Lorem ipsum dolor sit amet.</strong><span>Ut enim ad minim veniam, quis nostrud exercitation ullamco laboris nisi ut aliquip ex ea commodo consequat.</span></div></li>
      <li><i></i><div><strong>Lorem ipsum dolor sit amet.</strong><span>Ut enim ad minim veniam, quis nostrud exercitation ullamco laboris nisi ut aliquip ex ea commodo consequat.</span></div></li>
    </ul>
  </aside>

  <div class="abs goup">
    <span class="arrow"><svg width="14" height="10" viewBox="0 0 14 10"><path d="M2 8 L7 3 L12 8" stroke="#fff" stroke-width="2.5" fill="none"/></svg></span>
    <span class="label">Go Up!</span>
  </div>

  <footer class="abs footer">
    <div class="abs fcol" style="left:52px"><h4>Links</h4><ul><li>Home</li><li>Request a Bid</li></ul></div>
    <div class="abs fcol" style="left:205px"><h4>Get to Know Us</h4><ul><li>About Us</li><li>Our Services</li><li>Our Employes</li><li>Our CEO</li></ul></div>
    <div class="abs fcol" style="left:393px"><h4>Why&nbsp; Us</h4><ul><li>Why Choose Tidy Haven?</li><li>What Our Customers Are Saying</li><li>Testimonials</li><li>Special Offers</li></ul></div>
    <div class="abs fbrand">
      <div class="brand-row"><span class="brand-mark"></span><span class="brand-name">Tidy Haven</span></div>
      <div class="tag">Quality Commercial &amp; Residential Cleaning</div>
    </div>
    <address class="abs faddr">Tidy Haven 4120<br>Maple Ridge Avenue<br>Suite 310<br>Springfield, Oregon<br>97477</address>
    <div class="abs badge" role="img" aria-label="Accreditation badge"></div>
    <p class="abs fine">Our team cleans homes and offices across the region with care, trained staff and eco friendly products. Every visit is backed by our satisfaction promise, clear pricing and friendly support. Book a visit today and enjoy a spotless space without hidden fees or extra charges at any time.<br>© Copyright 2014 Tidy Haven</p>
    <div class="abs socials footer-social"><i class="social"></i><i class="social"></i><i class="social"></i><i class="social"></i></div>
  </footer>
</div>

</body>
</html>
```